Business Card Design

We are a residential half way house for the addict ,the alcoholic and dual diagnosed in recovery.
i house both men and woman age 18+

Industry/Entity Type

Residential

```html
<!DOCTYPE html>
<html lang="en">
<head>
<meta charset="utf-8">
<title>Harbor Light Recovery Residence – Business Card</title>
<link href="https://fonts.googleapis.com/css2?family=Dosis:wght@600&family=Arimo:wght@400&display=swap" rel="stylesheet">
<style>
  :root {
    --band: #353c40;
    --ink: #3a3f42;
    --brand-ink: #3d4447;
    --mark: #4a5356;
    --ring: #dcdfe0;
    --paper: #ffffff;
  }
  * { margin: 0; padding: 0; box-sizing: border-box; }
  html, body {
    width: 1200px; height: 686px; overflow: hidden; background: var(--paper);
  }
  .card {
    position: relative; width: 1200px; height: 686px; overflow: hidden;
    background: var(--paper); color: var(--ink);
  }
  .band { position: absolute; left: 0; width: 100%; background: var(--band); }
  .band--top { top: 0; height: 34px; }
  .band--bottom { bottom: 0; height: 35px; }

  .brand { position: absolute; left: 143px; top: 134px; display: flex; align-items: center; gap: 32px; }
  .brand__dot { width: 64px; height: 64px; border-radius: 50%; background: var(--mark); }
  .brand__name {
    font-family: "Arimo", sans-serif; font-weight: 400; font-size: 44px;
    color: var(--brand-ink); line-height: 1;
  }

  .backdrop-ring { position: absolute; left: 462px; top: 335px; }

  .accent-bar { position: absolute; left: 0; top: 318px; width: 59px; height: 25px; background: var(--band); }

  .contact { position: absolute; left: 82px; top: 310px; }
  .contact__name {
    font-family: "Dosis", sans-serif; font-weight: 600; font-size: 36px;
    line-height: 40px; color: var(--ink); letter-spacing: 0.5px;
  }
  .contact__role, .contact__line, .address__line {
    font-family: "Arimo", sans-serif; font-weight: 400; font-size: 30px; line-height: 1; color: var(--ink);
  }
  .contact__role { margin-top: 4px; }
  .contact__line { margin-top: 16px; }
  .contact__line + .contact__line { margin-top: 17px; }

  .address { position: absolute; left: 745px; top: 446px; }
  .address__line + .address__line { margin-top: 20px; }
</style>
</head>
<body>
  <div class="card">
    <div class="band band--top"></div>

    <div class="brand">
      <span class="brand__dot"></span>
      <span class="brand__name">Harbor Light Recovery Residence</span>
    </div>

    <svg class="backdrop-ring" width="256" height="256" viewBox="0 0 256 256" aria-hidden="true">
      <circle cx="128" cy="128" r="120" fill="none" stroke="var(--ring)" stroke-width="12"/>
    </svg>

    <div class="accent-bar"></div>

    <div class="contact">
      <p class="contact__name">Dana Whitfield</p>
      <p class="contact__role">Owner</p>
      <p class="contact__line">561-555-0142</p>
      <p class="contact__line">561-555-0143</p>
      <p class="contact__line">561-555-0187</p>
      <p class="contact__line">danawhitfield@mailbox.com</p>
    </div>

    <div class="address">
      <p class="address__line">2418 Palmetto Rd</p>
      <p class="address__line">Lake Harbor</p>
      <p class="address__line">Fla 33407</p>
    </div>

    <div class="band band--bottom"></div>
  </div>
</body>
</html>
```